Design a Banner for wood website

Need a 1345px by 400px banner (layered photoshop file w/png) created for a company that sells ipe wood decking.
- Must show ipe wood images within the design
- Must have text stating "Get a Quote!"

```html
<!DOCTYPE html>
<html lang="en">
<head>
<meta charset="UTF-8">
<title>Ipe Wood Decking Banner</title>
<link href="https://fonts.googleapis.com/css2?family=Federo&family=Arimo:wght@400&display=swap" rel="stylesheet">
<style>
  :root {
    --wood-deep: #4a200e;
    --wood-mid: #6e3218;
    --wood-warm: #7d3b1c;
    --title-white: #ffffff;
    --title-shadow: #0d0604;
    --button-fill: #3a190b;
    --button-border: #ffffff;
    --accent-yellow: #f4c400;
    --button-text: #ffffff;
  }
  html, body {
    margin: 0;
    padding: 0;
    overflow: hidden;
    background: var(--wood-deep);
  }
  .banner {
    position: relative;
    width: 1200px;
    height: 357px;
    overflow: hidden;
  }
  .banner__wood {
    position: absolute;
    inset: 0;
    background:
      linear-gradient(180deg, rgba(0,0,0,0.18) 0%, rgba(0,0,0,0) 35%, rgba(0,0,0,0) 65%, rgba(0,0,0,0.22) 100%),
      radial-gradient(ellipse at 50% 45%, var(--wood-warm) 0%, var(--wood-mid) 55%, var(--wood-deep) 100%);
  }
  .banner__title {
    position: absolute;
    left: 0;
    right: 0;
    top: 112px;
    margin: 0;
    text-align: center;
    font-family: "Federo", sans-serif;
    font-weight: 400;
    font-size: 98px;
    line-height: 1;
    letter-spacing: 3px;
    color: var(--title-white);
    text-shadow: 4px 3px 0 var(--title-shadow);
    white-space: nowrap;
  }
  .quote-button {
    position: absolute;
    left: 490px;
    top: 275px;
    width: 241px;
    height: 50px;
    box-sizing: border-box;
    border: 2px solid var(--button-border);
    border-radius: 25px;
    background: var(--button-fill);
    display: flex;
    align-items: center;
    justify-content: center;
    text-decoration: none;
  }
  .quote-button__arrows {
    position: absolute;
    inset: 0;
  }
  .quote-button__label {
    position: relative;
    font-family: "Arimo", sans-serif;
    font-size: 23px;
    color: var(--button-text);
    letter-spacing: 0.5px;
    margin-top: -2px;
  }
</style>
</head>
<body>
  <div class="banner">
    <div class="banner__wood" role="img" aria-label="Close-up of warm brown ipe wood grain"></div>
    <h1 class="banner__title">IPE WOOD DECKING</h1>
    <a class="quote-button" href="#quote">
      <svg class="quote-button__arrows" width="237" height="46" viewBox="0 0 237 46" aria-hidden="true">
        <polygon points="16,23 34,10 34,36" fill="var(--accent-yellow)"/>
        <polygon points="221,23 203,10 203,36" fill="var(--accent-yellow)"/>
        <path d="M40 37 Q120 33 200 35 Q120 38 40 37 Z" fill="var(--accent-yellow)"/>
      </svg>
      <span class="quote-button__label">GET A QUOTE</span>
    </a>
  </div>
</body>
</html>
```